Harbor Nightclub

Nightclub flyer., digital single sided, for KV and PX. I included samples of some previous flyers we've used. Sample Info:
HARBOR
FRIDAYS
FRI MAY 1 2020
DJ VORTAN (club floor)
DJ RUZO & DJ TAV (residents on the lounge floor)
4217 Marlow Avenue Sacramento
www.harborvenuehall.example for list/VIP inquiries

Target Market(s)

Upscale top 40 crowd but want some cool and artsy like the examples included.

Font styles to use
Sans Serif

Requirements
Must have
• Harbor Logo
Nice to have
• Would be nice if the flyer can be incorporated later with DJ photos (sometimes we will add dj photos to pixagram etc). Would like a big city type of feel.
Should not have
• Nothing too sexual.

```html
<!DOCTYPE html>
<html lang="en">
<head>
<meta charset="utf-8">
<title>Harbor Fridays – Harbor Nightclub</title>
<link rel="stylesheet" href="https://fonts.googleapis.com/css2?family=Montserrat:wght@600&family=Questrial&display=swap">
<style>
  :root {
    --night: #231b47;
    --violet: #3b2c8c;
    --plum: #6a2a78;
    --magenta: #d4185f;
    --amber: #f0a02e;
    --cyan: #2bb6e0;
    --white: #ffffff;
    --frame: rgba(255, 255, 255, 0.28);
  }
  * { margin: 0; padding: 0; box-sizing: border-box; }
  html, body { width: 846px; height: 1200px; overflow: hidden; background: var(--night); }
  .flyer {
    position: relative;
    width: 846px;
    height: 1200px;
    overflow: hidden;
    color: var(--white);
    font-family: "Questrial", sans-serif;
  }
  .street-scene {
    position: absolute; inset: 0;
    background:
      radial-gradient(ellipse 60% 35% at 30% 62%, rgba(212,24,95,0.45), transparent 70%),
      radial-gradient(ellipse 40% 30% at 85% 35%, rgba(60,110,230,0.45), transparent 70%),
      linear-gradient(180deg, #3a2c92 0%, #4b2a8a 30%, #5a2a7c 50%, #4a2466 65%, #2a1e50 82%, var(--night) 100%);
  }
  .decor { position: absolute; inset: 0; width: 846px; height: 1200px; }
  .headline {
    position: absolute; left: 0; width: 846px; text-align: center;
  }
  .title {
    top: 222px;
    font-family: "Montserrat", sans-serif;
    font-weight: 600;
    font-size: 118px;
    letter-spacing: 6px;
    line-height: 1;
  }
  .subtitle { top: 353px; font-size: 40px; letter-spacing: 30px; text-indent: 30px; }
  .dj-name {
    font-family: "Montserrat", sans-serif;
    font-weight: 600;
    font-size: 47px;
    letter-spacing: 4px;
  }
  .dj-club { top: 470px; }
  .floor { font-size: 25px; letter-spacing: 18px; text-indent: 18px; }
  .floor-club { top: 532px; }
  .dj-lounge { top: 611px; }
  .floor-lounge { top: 673px; }
  .brand-name { top: 851px; font-size: 40px; letter-spacing: 4px; }
  .event-date { top: 922px; font-size: 30px; letter-spacing: 12px; text-indent: 12px; }
  .event-address { top: 966px; font-size: 21px; letter-spacing: 8px; text-indent: 8px; }
  .list-label { top: 1068px; font-size: 21px; letter-spacing: 8px; text-indent: 8px; }
  .site-url { top: 1105px; font-size: 21px; letter-spacing: 7px; text-indent: 7px; }
</style>
</head>
<body>
<main class="flyer">
  <div class="street-scene" role="img" aria-label="Night street photo of a crowd lining up outside the club with a car in the foreground, tinted purple and magenta"></div>

  <svg class="decor" viewBox="0 0 846 1200" aria-hidden="true">
    <defs>
      <linearGradient id="beam" x1="0" y1="0" x2="1" y2="1">
        <stop offset="0" stop-color="#d4185f" stop-opacity="0"/>
        <stop offset="0.5" stop-color="#d4185f" stop-opacity="0.22"/>
        <stop offset="1" stop-color="#2bb6e0" stop-opacity="0"/>
      </linearGradient>
    </defs>

    <polygon class="light-beam" points="0,150 846,470 846,560 0,240" fill="url(#beam)"/>

    <rect class="frame" x="20" y="20" width="806" height="1160" fill="none" stroke="var(--frame)" stroke-width="1"/>

    <g class="corner-ticks" stroke="#ffffff" stroke-width="2">
      <line x1="20" y1="20" x2="60" y2="20"/>
      <line x1="20" y1="20" x2="20" y2="60"/>
      <line x1="826" y1="1180" x2="786" y2="1180"/>
      <line x1="826" y1="1180" x2="826" y2="1140"/>
    </g>

    <g class="dividers" stroke="#ffffff" stroke-opacity="0.5" stroke-width="1">
      <line x1="393" y1="443" x2="453" y2="443"/>
      <line x1="393" y1="742" x2="453" y2="742"/>
      <line x1="393" y1="1036" x2="453" y2="1036"/>
    </g>

    <circle class="brand-mark" cx="423" cy="800" r="40" fill="none" stroke="#ffffff" stroke-width="4"/>
  </svg>

  <h1 class="headline title">HARBOR</h1>
  <p class="headline subtitle">FRIDAYS</p>

  <p class="headline dj-name dj-club">DJ VORTAN</p>
  <p class="headline floor floor-club">CLUB FLOOR</p>

  <p class="headline dj-name dj-lounge">DJ RUZO &amp; DJ TAV</p>
  <p class="headline floor floor-lounge">LOUNGE FLOOR</p>

  <p class="headline brand-name">HARBOR</p>

  <p class="headline event-date">FRI | MAY 1 2020</p>
  <p class="headline event-address">4217 MARLOW AVENUE SACRAMENTO</p>

  <p class="headline list-label">FOR LIST/VIP INQUIRIES</p>
  <p class="headline site-url">WWW.HARBORVENUEHALL.EXAMPLE</p>
</main>
</body>
</html>
```